Simple and clean webdesign for personal homepage

Trying to create a simple and clean webdesign for my personal homepage. Going to use a static site builder with templates to build the site. I want it to have multiple pages - like an about me, blog and resume. I just need something very basic I can customize. I want the main colors to be purple, black and white. I am open to other color palettes too but since purple is my favorite color I want that to be one of the main colors.

The site be mostly text driven. Might have some images in the body text but I want the site design to be light and lean.

Industry/Entity Type

Personal Homepage.

Coding

Coded - Design and coding required

Number of Pages Required

1 page

Font styles to use
Sans Serif

Colors
6B429C
8869AF
B7A5CE
E3DAEB
F3F0F8

Requirements
Must have
• Clean design. Purple used as a color. HTML template.
Nice to have
• Responsive

```html
<!DOCTYPE html>
<html lang="en">
<head>
<meta charset="utf-8">
<title>Avery Lind — Graphic Designer</title>
<link rel="stylesheet" href="https://fonts.googleapis.com/css2?family=Poppins:wght@400;500;600;700&display=swap">
<style>
:root{
  --accent:#5b3be8;
  --accent-soft:#efebfb;
  --ink:#2f2f33;
  --muted:#7a7a84;
  --hero-bg:#f7f6fa;
  --card:#ffffff;
  --footer:#424244;
  --photo-b:#2b2b30;
  --thumb-a:#e8e9ef;
  --thumb-b:#2a3a5c;
}
*{margin:0;padding:0;box-sizing:border-box}
html,body{width:1200px;height:3536px;overflow:hidden}
body{position:relative;background:#fff;font-family:"Poppins",sans-serif;color:var(--ink)}
.abs{position:absolute}
a{color:inherit;text-decoration:none}

/* nav */
.hero-band{left:0;top:0;width:1200px;height:537px;background:var(--hero-bg)}
.brand{left:250px;top:22px;display:flex;align-items:center;gap:6px;font-size:11px;font-weight:600;color:var(--accent)}
.brand-dot{width:12px;height:12px;border-radius:50%;background:var(--accent)}
.nav{left:423px;top:18px;display:flex;gap:6px;font-size:9px;font-weight:500;text-transform:uppercase;white-space:nowrap}
.nav a{padding:6px 12px 12px}
.nav a.active{color:var(--accent);border-bottom:1.5px solid var(--accent)}
.hire{left:873px;top:19px;width:78px;height:25px;border-radius:13px;background:var(--accent);color:#fff;font-size:8px;font-weight:500;display:flex;align-items:center;justify-content:center;gap:4px}

/* hero */
.eyebrow{font-size:10px;color:var(--accent);text-transform:uppercase;letter-spacing:.2px}
.hero-title{left:250px;top:176px;font-size:39px;line-height:48.5px;font-weight:700;color:var(--ink);letter-spacing:-.3px}
.btn{background:var(--accent);color:#fff;border-radius:24px;font-size:8.5px;font-weight:500;text-transform:uppercase;display:flex;align-items:center;justify-content:center;gap:4px}
.cv{left:415px;top:420px;font-size:9px;text-transform:uppercase;display:flex;gap:8px;align-items:center}
.hero-circle{left:594px;top:90px;width:356px;height:356px;border-radius:50%;background:var(--accent-soft)}
.hero-photo{left:618px;top:93px;width:302px;height:444px;border-radius:150px 150px 0 0;background:linear-gradient(180deg,#c99e85 0%,#b08470 25%,var(--photo-b) 45%,var(--photo-b) 100%)}
.dot{border-radius:50%;background:var(--accent)}

/* stats */
.stat{width:180px;text-align:center}
.stat b{display:block;font-size:40px;font-weight:600;line-height:1}
.stat span{display:block;margin-top:10px;font-size:10px;color:var(--muted);text-transform:uppercase}

/* section heads */
.sec-head{left:0;width:1200px;text-align:center}
.sec-title{font-size:25px;font-weight:700;letter-spacing:-.2px}
.sec-desc{width:380px;margin:0 auto;font-size:10px;line-height:18px;color:var(--muted)}

/* services */
.service{top:913px;width:226px;height:200px;background:var(--card);border-radius:12px;box-shadow:0 18px 40px rgba(40,30,90,.09);text-align:center;padding:28px 26px 0}
.service svg{display:block;margin:0 auto}
.service h3{margin-top:22px;font-size:12px;font-weight:600}
.service p{margin-top:10px;font-size:10px;line-height:17.5px;color:var(--muted)}

/* about */
.about-circle{left:266px;top:1209px;width:286px;height:286px;border-radius:50%;background:var(--accent-soft)}
.about-photo{left:313px;top:1208px;width:198px;height:292px;border-radius:99px 99px 0 0;background:linear-gradient(180deg,#c99e85 0%,#b08470 28%,var(--photo-b) 48%,var(--photo-b) 100%)}
.about-title{left:638px;top:1232px;font-size:25px;line-height:31px;font-weight:700}
.about-text{left:638px;top:1305px;width:312px;font-size:10px;line-height:18px;color:var(--muted)}
.checks{left:638px;top:1364px;list-style:none;font-size:10px;color:var(--muted)}
.checks li{display:flex;align-items:center;gap:11px;height:28.5px}

/* portfolio */
.work{width:344px;height:332px;background:var(--card);border-radius:12px;box-shadow:0 16px 40px rgba(40,30,90,.08);overflow:hidden}
.thumb{height:229px}
.thumb.navy{background:linear-gradient(135deg,var(--thumb-a) 0%,var(--thumb-a) 25%,var(--thumb-b) 40%,var(--thumb-b) 65%,var(--thumb-a) 80%)}
.thumb.light{background:linear-gradient(135deg,#e9e9ec 0%,#f7f6f2 45%,#d8d4c8 70%,#eeeeef 100%)}
.work h3{margin:17px 19px 0;font-size:11.5px;font-weight:600}
.work p{margin:10px 19px 0;font-size:10px;line-height:17.5px;color:var(--muted)}

/* testimonial */
.quote-box{left:250px;top:2569px;width:700px;height:357px;background:var(--hero-bg);border-radius:14px}
.quote{left:356px;top:2660px;width:460px;font-size:21px;line-height:30px;color:#3c3c44}
.avatar{left:355px;top:2766px;width:36px;height:36px;border-radius:50%;background:linear-gradient(135deg,#d7d9e2,#aeb3c2)}
.who{left:406px;top:2773px;font-size:11px;font-weight:500}
.who small{display:block;font-size:9px;font-weight:400;color:var(--muted)}
.pager{left:586px;top:2833px;display:flex;gap:8px}
.pager i{width:4px;height:4px;border-radius:50%;background:#c9c9d2}
.pager i.on{background:#333}

/* clients */
.clients-title{left:250px;top:3038px;font-size:25px;line-height:32px;font-weight:700}
.clients-text{left:250px;top:3112px;width:320px;font-size:10px;line-height:18px;color:var(--muted)}
.client{top:3070px;display:flex;align-items:center;gap:8px;font-size:18px;font-weight:500;color:#8a8a8e}
.client i{width:16px;height:16px;border-radius:3px;background:#8a8a8e}

/* footer */
.footer{left:25px;top:3243px;width:1150px;height:293px;background:var(--footer);border-radius:14px 14px 0 0;color:#fff}
.f-brand{left:225px;top:64px;display:flex;align-items:center;gap:7px;font-size:16px;font-weight:500}
.f-brand i{width:18px;height:18px;border-radius:50%;background:#fff}
.f-text{left:225px;top:98px;width:215px;font-size:10px;line-height:18px}
.f-contact{left:700px;top:67px;font-size:10px;display:flex;flex-direction:column;gap:11px}
.f-contact div{display:flex;align-items:center;gap:6px}
.socials{display:flex;gap:12px}
.socials i{width:10px;height:10px;border-radius:50%;background:#fff}
.f-rule{left:225px;top:192px;width:700px;height:1px;background:#5f5f62}
.f-links{left:225px;top:228px;display:flex;gap:13px;font-size:8.5px;font-weight:500;text-transform:uppercase}
.f-credit{right:225px;top:227px;font-size:9.5px;white-space:nowrap}
</style>
</head>
<body>

<!-- header & hero -->
<div class="abs hero-band"></div>
<div class="abs brand"><span class="brand-dot"></span>LUMENFOLIO</div>
<nav class="abs nav">
  <a class="active" href="#">Home</a><a href="#">About Us</a><a href="#">Services</a><a href="#">Pages ▾</a><a href="#">Contact Us</a>
</nav>
<a class="abs hire" href="#">Hire Me
  <svg width="9" height="9" viewBox="0 0 10 10"><path d="M0 4.5 10 0 7 10 5 6Z" fill="#fff"/></svg>
</a>

<p class="abs eyebrow" style="left:250px;top:145px">Avery Lind</p>
<h1 class="abs hero-title">Hello, my<br>name's Avery.<br>I'm Graphic<br>Designer.</h1>
<a class="abs btn" href="#" style="left:257px;top:406px;width:133px;height:40px">
  <svg width="9" height="7" viewBox="0 0 9 7"><rect x=".5" y=".5" width="8" height="6" fill="none" stroke="#fff"/><path d="M.5 .5 4.5 4 8.5 .5" fill="none" stroke="#fff"/></svg>Contact Me</a>
<a class="abs cv" href="#">
  <svg width="7" height="9" viewBox="0 0 7 9"><path d="M0 0h5l2 2v7H0Z" fill="#333"/></svg>Download CV</a>

<div class="abs hero-circle"></div>
<div class="abs hero-photo" role="img" aria-label="Portrait photo of the designer in a black t-shirt, arms crossed"></div>
<div class="abs dot" style="left:875px;top:130px;width:10px;height:10px"></div>
<div class="abs dot" style="left:583px;top:257px;width:19px;height:19px"></div>
<div class="abs dot" style="left:919px;top:351px;width:18px;height:18px"></div>
<svg class="abs" style="left:538px;top:403px" width="48" height="50" viewBox="0 0 48 50"><path d="M0 22 46 0 38 48Z" fill="var(--accent)"/></svg>

<!-- stats -->
<div class="abs stat" style="left:242px;top:628px"><b>100+</b><span>Projects</span></div>
<div class="abs stat" style="left:421px;top:628px"><b>24+</b><span>Awards</span></div>
<div class="abs stat" style="left:599px;top:628px"><b>70+</b><span>Clients</span></div>
<div class="abs stat" style="left:778px;top:628px"><b>10</b><span>Experience</span></div>

<!-- services -->
<svg class="abs" style="left:604px;top:758px" width="42" height="40" viewBox="0 0 42 40"><path d="M0 20 42 0 36 40Z" fill="var(--accent-soft)"/></svg>
<div class="abs sec-head" style="top:776px">
  <p class="eyebrow">Avery Lind</p>
  <h2 class="sec-title" style="margin-top:10px">What I Do For My Customer.</h2>
  <p class="sec-desc" style="margin-top:12px">Lorem ipsum dolor sit amet, consectetur adipiscing elit. Ut elit tellus, luctus nec ullamcorper mattis.</p>
</div>

<article class="abs service" style="left:250px">
  <svg width="20" height="20" viewBox="0 0 20 20"><path d="M10 2 18 8 15 18H5L2 8Z" fill="none" stroke="var(--accent)" stroke-width="1.4"/></svg>
  <h3>UI/UX Design</h3>
  <p>Lorem ipsum dolor sit amet, consectetur adipiscing elit. Ut elit tellus, luctus nec ullamcorper mattis,.</p>
</article>
<article class="abs service" style="left:487px">
  <svg width="20" height="20" viewBox="0 0 20 20"><path d="M1 10Q10 1 19 10Q10 19 1 10Z" fill="none" stroke="var(--accent)" stroke-width="1.4"/><circle cx="10" cy="10" r="3" fill="none" stroke="var(--accent)" stroke-width="1.4"/></svg>
  <h3>App Development</h3>
  <p>Lorem ipsum dolor sit amet, consectetur adipiscing elit. Ut elit tellus, luctus nec ullamcorper mattis,.</p>
</article>
<article class="abs service" style="left:725px">
  <svg width="20" height="20" viewBox="0 0 20 20"><path d="M10 2 18 6V14L10 18 2 14V6ZM2 6 10 10 18 6M10 10V18" fill="none" stroke="var(--accent)" stroke-width="1.4"/></svg>
  <h3>Web Development</h3>
  <p>Lorem ipsum dolor sit amet, consectetur adipiscing elit. Ut elit tellus, luctus nec ullamcorper mattis,.</p>
</article>

<!-- about -->
<div class="abs about-circle"></div>
<div class="abs about-photo" role="img" aria-label="Portrait photo of the designer smiling, arms crossed"></div>
<svg class="abs" style="left:616px;top:1181px" width="46" height="32" viewBox="0 0 46 32"><path d="M0 14 46 0 40 32Z" fill="var(--accent-soft)"/></svg>
<p class="abs eyebrow" style="left:638px;top:1207px">Avery Lind</p>
<h2 class="abs about-title">Know More About Me<br>From The Beginning.</h2>
<p class="abs about-text">Lorem ipsum dolor sit amet, consectetur adipiscing elit. Ut elit tellus, luctus nec ullamcorper mattis, pulvinar dapibus leo.</p>
<ul class="abs checks">
  <li><svg width="14" height="14" viewBox="0 0 14 14"><circle cx="7" cy="7" r="7" fill="var(--accent)"/><path d="M4 7.2 6.2 9.3 10 5" fill="none" stroke="#fff" stroke-width="1.5"/></svg>Lorem ipsum dolor sit amet const</li>
  <li><svg width="14" height="14" viewBox="0 0 14 14"><circle cx="7" cy="7" r="7" fill="var(--accent)"/><path d="M4 7.2 6.2 9.3 10 5" fill="none" stroke="#fff" stroke-width="1.5"/></svg>Lorem ipsum dolor sit amet const</li>
  <li><svg width="14" height="14" viewBox="0 0 14 14"><circle cx="7" cy="7" r="7" fill="var(--accent)"/><path d="M4 7.2 6.2 9.3 10 5" fill="none" stroke="#fff" stroke-width="1.5"/></svg>Lorem ipsum dolor sit amet const</li>
</ul>
<a class="abs btn" href="#" style="left:638px;top:1465px;width:106px;height:35px">Learn More</a>

<!-- portfolio -->
<svg class="abs" style="left:604px;top:1573px" width="42" height="40" viewBox="0 0 42 40"><path d="M0 20 42 0 36 40Z" fill="var(--accent-soft)"/></svg>
<div class="abs sec-head" style="top:1591px">
  <p class="eyebrow">Portfolio</p>
  <h2 class="sec-title" style="margin-top:10px">Selected Works.</h2>
  <p class="sec-desc" style="margin-top:12px">Lorem ipsum dolor sit amet, consectetur adipiscing elit. Ut elit tellus, luctus nec ullamcorper mattis.</p>
</div>

<article class="abs work" style="left:250px;top:1728px">
  <div class="thumb navy" role="img" aria-label="Collage of navy presentation slides for the Meridia template"></div>
  <h3>Meridia - Presentation Template</h3>
  <p>Lorem ipsum dolor sit amet, consectetur adipiscing elit. Ut elit tellus.</p>
</article>
<article class="abs work" style="left:606px;top:1728px">
  <div class="thumb light" role="img" aria-label="Collage of light corporate presentation slides for the Halvo template"></div>
  <h3>Halvo - Presentation Template</h3>
  <p>Lorem ipsum dolor sit amet, consectetur adipiscing elit. Ut elit tellus.</p>
</article>
<article class="abs work" style="left:250px;top:2072px">
  <div class="thumb light" role="img" aria-label="Collage of minimal white presentation slides for the Tesso template"></div>
  <h3>Tesso - Presentation Template</h3>
  <p>Lorem ipsum dolor sit amet, consectetur adipiscing elit. Ut elit tellus.</p>
</article>
<article class="abs work" style="left:606px;top:2072px">
  <div class="thumb navy" role="img" aria-label="Collage of navy presentation slides for the Meridia template"></div>
  <h3>Meridia - Presentation Template</h3>
  <p>Lorem ipsum dolor sit amet, consectetur adipiscing elit. Ut elit tellus.</p>
</article>

<a class="abs btn" href="#" style="left:535px;top:2447px;width:130px;height:35px">See All Projects</a>

<!-- testimonial -->
<div class="abs quote-box"></div>
<p class="abs quote">"Lorem ipsum dolor sit amet, consectetur adipiscing elit. Ut elit tellus, luctus nec ullamcorper mattis, pulvinar dapibus leo."</p>
<div class="abs avatar" role="img" aria-label="Client avatar"></div>
<p class="abs who">Marc Ellery<small>CEO</small></p>
<div class="abs pager"><i></i><i></i><i class="on"></i></div>

<!-- clients -->
<svg class="abs" style="left:228px;top:2998px" width="44" height="30" viewBox="0 0 44 30"><path d="M0 14 44 0 38 30Z" fill="var(--accent-soft)"/></svg>
<p class="abs eyebrow" style="left:250px;top:3012px">Clients</p>
<h2 class="abs clients-title">Our Previous Satisfied<br>Clients.</h2>
<p class="abs clients-text">Lorem ipsum dolor sit amet, consectetur adipiscing elit. Ut elit tellus, luctus nec ullamcorper mattis, pulvinar dapibus leo.</p>
<div class="abs client" style="left:634px"><i></i>Brightmark</div>
<div class="abs client" style="left:808px"><i></i>Solvane</div>

<!-- footer -->
<footer class="abs footer">
  <div class="abs f-brand"><i></i>LUMENFOLIO</div>
  <p class="abs f-text">Lorem ipsum dolor sit amet, consectetur adipiscing elit. Ut elit tellus, luctus nec ullamcorper mattis, pulvinar dapibus leo.</p>
  <div class="abs f-contact">
    <div><svg width="9" height="7" viewBox="0 0 9 7"><rect x=".5" y=".5" width="8" height="6" fill="none" stroke="#fff"/><path d="M.5 .5 4.5 4 8.5 .5" fill="none" stroke="#fff"/></svg>hello@lumenfolio.example</div>
    <div><svg width="9" height="9" viewBox="0 0 9 9"><path d="M1 1Q1 8 8 8L8 6 6 5 5 6Q3 5 3 4L4 3 3 1Z" fill="#fff"/></svg>(000) 5550 1200</div>
    <div class="socials"><i></i><i></i><i></i><i></i></div>
  </div>
  <div class="abs f-rule"></div>
  <nav class="abs f-links"><a href="#">Home</a><a href="#">About Us</a><a href="#">Services</a><a href="#">Contact Us</a></nav>
  <p class="abs f-credit">Lumenfolio Pagecraft Template Kit By Northpane</p>
</footer>

</body>
</html>
```